Web Design Project for Industrial Hemp

I'm launching a new company to grow Industrial Hemp and then to set up a manufacturing facility to process the crop each and every year. We require a complete end to end brand and livery suite and we will start with a web presence. We want to appeal to (a) Investors, Employees, Farmers, and consumers so as to engage with all our stakeholders. We want to create a whole new industry that becomes a game changer for environmentally friendly crop production. Hemp is gaining in popularity and credibility across the world!

Target Market(s)

Farmers to produce, Manufacturers who will purchase the raw materials, Investors who will invest in the project, Consumers who will buy Hemp Products

Industry/Entity Type

Industry

Requirements
Must have
• Environmentally Friendly
Carbon Neutral/Positive
Game Changer
Multi-Use Crop
50,000 products can be made from Hemp
Should not have
• Should avoid its relationship with cannabis but not ignore it! When the regulatory bodies acknowledge the benefits of cannabanoids, they will start to legalise the production of cannabis for sale on prescription

```html
<!DOCTYPE html>
<html lang="en">
<head>
<meta charset="utf-8">
<title>Verdant Field Fibres Ltd – Industrial Hemp</title>
<link href="https://fonts.googleapis.com/css2?family=Arimo:wght@400;700&display=swap" rel="stylesheet">
<style>
:root{
  --leaf-light:#6fae4a;
  --leaf-mid:#4f8a34;
  --nav-dark:#27401a;
  --panel-green:#4a7a2e;
  --panel-green-deep:#38621f;
  --orange-top:#ffa200;
  --orange-bottom:#ffc400;
  --page-bg:#ecebe6;
  --white:#ffffff;
  --ink:#111111;
  --title-green:#3f6b1f;
  --link-yellow:#ffc21a;
  --footer-top:#3f7426;
  --footer-bottom:#5c9434;
}
*{box-sizing:border-box;margin:0;padding:0}
html,body{width:1181px;height:1200px;overflow:hidden}
body{position:relative;background:var(--page-bg);font-family:"Arimo",Arial,sans-serif;color:var(--ink)}
.header-band{position:absolute;left:0;top:0;width:1181px;height:458px;
  background:radial-gradient(ellipse at 30% 20%,var(--leaf-light),transparent 60%),
             radial-gradient(ellipse at 80% 70%,#7dbb55,transparent 55%),
             linear-gradient(180deg,var(--leaf-mid),#5d9a3c 60%,#68a646)}
.brand{position:absolute;left:142px;top:44px;display:flex;align-items:center;gap:17px}
.brand-mark{width:65px;height:65px;border-radius:50%;border:3px solid var(--white)}
.brand-name{color:var(--white);font-size:36px;font-weight:400;letter-spacing:.2px}

.nav{position:absolute;left:142px;top:144px;width:884px;height:36px;background:var(--nav-dark);border-radius:6px 6px 0 0}
.nav-home{position:absolute;left:142px;top:136px;width:132px;height:45px;background:var(--white);border-radius:8px 8px 0 0;
  font-weight:700;font-size:19px;color:#3a2414;padding:17px 0 0 36px}
.nav-home::after{content:"";position:absolute;right:-16px;top:8px;border-left:16px solid var(--white);border-top:37px solid transparent}
.nav-links{position:absolute;top:153px;left:0;list-style:none}
.nav-links li{position:absolute;color:var(--white);font-weight:700;font-size:19px;white-space:nowrap}
.search{position:absolute;left:821px;top:149px;width:191px;height:23px;background:var(--white);border-radius:12px}

.panel{position:absolute;background:var(--white);border:1px solid #d6d5cf}
.hero{left:142px;top:180px;width:884px;height:369px;border-top:none}
.hero-tile{position:absolute;left:152px;width:277px;height:111px;color:var(--white);font-size:23px;line-height:23px;padding:24px 0 0 32px;
  background:linear-gradient(180deg,var(--panel-green),var(--panel-green-deep))}
.hero-tile.accent{color:var(--ink);background:linear-gradient(180deg,var(--orange-top),var(--orange-bottom));width:278px}
.hero-arrow{position:absolute;left:429px;top:312px}
.hero-photo{position:absolute;left:438px;top:201px;width:573px;height:332px;
  background:radial-gradient(ellipse at 35% 45%,#b0502f,transparent 40%),
             radial-gradient(ellipse at 75% 60%,#9c9c6a,transparent 35%),
             linear-gradient(90deg,#3a2410,#6b4a1c 50%,#4a3012)}

.side{left:142px;top:560px;width:287px;height:295px}
.topic-menu{position:absolute;left:156px;top:574px;width:257px;height:267px;list-style:none;padding-top:13px;
  background:linear-gradient(180deg,#5d8f3a,var(--panel-green-deep))}
.topic-menu li{color:var(--white);font-size:16.5px;height:26.7px;line-height:25px;padding-left:36px;border-bottom:1px dotted rgba(255,255,255,.55)}
.topic-menu li:last-child{border-bottom:none}

.intro{left:439px;top:560px;width:587px;height:295px;padding:15px 27px 0 27px}
.intro h1{color:var(--title-green);font-size:22.5px;font-weight:700;margin-bottom:5px}
.intro p{font-size:14.4px;line-height:14.8px;margin-bottom:8px}
.more{position:absolute;right:42px;bottom:27px;color:var(--title-green);font-weight:700;font-size:14.5px}

.audiences{left:142px;top:869px;width:884px;height:157px}
.audience{position:absolute;top:878px;width:277px;height:139px;color:var(--white);padding:26px 0 0 30px;overflow:hidden;
  background:linear-gradient(180deg,#5a8d38,var(--panel-green-deep))}
.audience h2{position:relative;z-index:1;font-size:22.5px;font-weight:700;margin-bottom:4px}
.audience p{position:relative;z-index:1;font-size:14.4px;line-height:14.5px;width:140px}
.audience .learn{position:relative;z-index:1;color:var(--link-yellow);font-size:14.4px;margin-top:10px;display:block}
.audience.consumers{padding-left:22px}
.audience.consumers p{width:150px}
.portrait{position:absolute;right:0;top:0;width:95px;height:139px;
  background:linear-gradient(180deg,rgba(255,255,255,.10),rgba(0,0,0,.12))}

.footer{position:absolute;left:0;top:1049px;width:1181px;height:151px;background:linear-gradient(180deg,var(--footer-top),var(--footer-bottom))}
.social{position:absolute;left:154px;top:1089px;display:grid;grid-template-columns:repeat(3,38px);gap:9px 13px}
.social span{width:38px;height:38px;border:2px solid #e8e8e8;background:#8fb873}
.footer-links{position:absolute;top:1090px;list-style:none}
.footer-links li{color:var(--white);font-size:16px;line-height:16px}
.signup{position:absolute;left:789px;top:1095px;color:var(--white);font-size:16.5px}
.signup-form{position:absolute;left:789px;top:1121px;width:230px;height:24px;background:var(--white);border:2px solid #e8e8e8;display:flex}
.signup-form span{flex:1;font-size:14px;padding:3px 9px;color:#222}
.signup-form b{width:57px;background:#ffd21a;font-size:15px;text-align:center;line-height:20px}
.copyright{position:absolute;left:770px;top:1156px;color:var(--white);font-size:15.5px}
</style>
</head>
<body>
<div class="header-band" role="img" aria-label="Field of green hemp leaves"></div>
<div class="brand"><span class="brand-mark"></span><span class="brand-name">Verdant Field Fibres Ltd</span></div>

<div class="nav"></div>
<div class="nav-home">Home</div>
<ul class="nav-links">
  <li style="left:290px">About</li>
  <li style="left:369px">Investors</li>
  <li style="left:482px">Farmers</li>
  <li style="left:591px">Consumers</li>
  <li style="left:728px">Contact</li>
</ul>
<div class="search"></div>
<svg style="position:absolute;left:992px;top:154px" width="13" height="13" viewBox="0 0 13 13"><circle cx="7.5" cy="5.5" r="3.6" fill="none" stroke="#999" stroke-width="1.5"/><line x1="5" y1="8" x2="1.5" y2="11.5" stroke="#999" stroke-width="1.8"/></svg>

<div class="panel hero"></div>
<div class="hero-tile" style="top:201px">Environmentally<br>Friendly and<br>Multi-Use Crop</div>
<div class="hero-tile accent" style="top:312px">Over 50,000<br>products can be<br>made from Hemp</div>
<svg class="hero-arrow" width="33" height="111" viewBox="0 0 33 111"><polygon points="0,0 0,111 33,55.5" fill="#ffb300"/></svg>
<div class="hero-tile" style="top:423px;height:110px">Excellent food source,<br>providing nearly<br>complete nutrition</div>
<div class="hero-photo" role="img" aria-label="Photo: woman in a red top with hemp products such as cereal, a backpack, shoes and lip balm"></div>

<div class="panel side"></div>
<ul class="topic-menu">
  <li>History</li><li>Body Care</li><li>Building Material</li><li>Clothing / Textiles</li><li>Food Source</li>
  <li>Fuel / Energy</li><li>Livestock/Bedding/Feed</li><li>Environment / Soil</li><li>Economy and Politics</li>
</ul>

<div class="panel intro">
  <h1>Why Hemp?</h1>
  <p>For most of human existence, hemp has provided food, fuel, clothing and shelter for people all over the world. It is an organism that holds the greatest promise for renewable/sustainable food, fuel, clothing and shelter accessible to the widest possible range of people.</p>
  <p>Compared to cotton, hemp textiles are stronger, more durable, use one third the amount of water, and require no crop chemicals. Cotton uses 25-30% of the worlds toxic crop chemicals. It can also make most building materials, including caulking, cement, fiberboard, flooring, insulation, paneling, particleboard, plaster, plywood, stucco, mortar, and biodegradable plastic.</p>
  <p>Hemp farming requires no toxic pesticides, herbicides, fungicides, and no fertilizer if grown in a proper crop rotation. Hemp is the ultimate green crop. It produces food, fiber, pulp, and cellulose for thousands of industries without any toxic chemicals needed in any of the processing.</p>
  <span class="more">learn more ▸</span>
</div>

<div class="panel audiences"></div>
<div class="audience" style="left:154px">
  <div class="portrait" role="img" aria-label="Photo: investor in a dark business suit"></div>
  <h2>Investors</h2><p>Industrial Hemp is a sector Primed for Growth.</p><span class="learn">learn more ▸</span>
</div>
<div class="audience" style="left:445px">
  <div class="portrait" role="img" aria-label="Photo: farmer in a cap and green t-shirt"></div>
  <h2>Farmers</h2><p>Hemp is the most versatile &amp; adaptable crop plant on earth.</p><span class="learn">learn more ▸</span>
</div>
<div class="audience consumers" style="left:737px">
  <div class="portrait" role="img" aria-label="Photo: consumer in a white polo shirt"></div>
  <h2>Consumers</h2><p>Hemp products include seed for foods, oil, resin, cloth and fuel.</p><span class="learn">learn more ▸</span>
</div>

<footer class="footer"></footer>
<div class="social" aria-label="Social network links">
  <span></span><span></span><span></span><span></span><span></span><span></span>
</div>
<ul class="footer-links" style="left:358px"><li>Our Team</li><li>Disclaimer</li><li>Privacy Policies</li><li>Terms of use</li><li>Contact us</li></ul>
<ul class="footer-links" style="left:505px"><li>Our Services</li><li>Our Newsletter</li><li>Questions</li><li>Resources</li><li>Our Forum</li></ul>
<ul class="footer-links" style="left:641px"><li>Directory</li><li>Advertise</li><li>Media</li><li>Events</li><li>Feedbacks</li></ul>
<div class="signup">Sign up for our Newsletter</div>
<div class="signup-form"><span>your email</span><b>JOIN</b></div>
<div class="copyright">© 2013. Verdant Field Fibres Ltd</div>
</body>
</html>
```